Energieausweis
Zielgruppe
Zielgruppe sind Immobilieninteressenten - Verwendung in einem Immobilienmagazin und im Internet.
Aufgabenstellung
Ab dem 1. Mai muss in Deutschland die Energie-Effizienzklasse bei Immobilienangeboten mit veröffentlicht werden. Das kann man nüchtern in Zahlen darstellen, aber auch in einer netten Grafik. In der Anlage finden 2 von uns gekaufte Pixbarun-Bilder. Das Bild mit dem Männchen ist eine sehr nette Idee. Da wir in unserem Logo auch ein Männchen haben, bietet es sich an, ein LindenHaus-Männchen zusammen mit der bunten Grafik zu gestalten. (Das Pixbarun-Bild soll nur die Idee erklären - bitte nicht verwenden). Wenn die Grafik fertig ist, legen wir einen Pfeil zur Kennzeichnung der jeweiligen Energieklasse hinzu. Das heisst, wir haben dann für jede Energieklasse eine entsprechende Vorlage und dem richtig platzierten Pfeil. Weiter finden sie in der Anlage unser Firmenlogo zur freuen Verwendung.

```html
<!DOCTYPE html>
<html lang="de">
<head>
<meta charset="utf-8">
<title>Energieausweis – Vorlagen A bis G</title>
<link href="https://fonts.googleapis.com/css2?family=Open+Sans:wght@400;600;700&display=swap" rel="stylesheet">
<style>
  :root {
    --bg: #ffffff;
    --house-grey: #e4e4e5;
    --brand-blue: #1d4f8c;
    --title-blue: #215d9c;
    --ink: #1a1a1a;
    --marker: #0b0b0b;
    --figure: #0f4a7a;
    --class-a: #0b6a2f;
    --class-b: #2d9b34;
    --class-c: #9dbb0c;
    --class-d: #e0d90c;
    --class-e: #ecb700;
    --class-f: #ec7800;
    --class-g: #e2231a;
  }
  html, body {
    margin: 0;
    width: 1200px;
    height: 2792px;
    overflow: hidden;
    background: var(--bg);
    font-family: "Open Sans", Arial, sans-serif;
  }
  .canvas { position: relative; width: 1200px; height: 2792px; }
  .label-card { position: absolute; width: 515px; height: 618px; }
  .house-shape { fill: var(--house-grey); }
  .brand-mark { fill: var(--brand-blue); }
  .brand-name { fill: var(--brand-blue); font-size: 36px; font-weight: 600; }
  .bar-letter { fill: #ffffff; font-size: 19px; font-weight: 600; text-anchor: middle; }
  .figure-area { fill: var(--figure); }
  .marker-shape { fill: var(--marker); }
  .marker-letter { fill: #ffffff; font-size: 19px; font-weight: 700; text-anchor: middle; }
  .caption { fill: var(--ink); font-size: 16px; font-weight: 600; text-anchor: end; }
  .title { fill: var(--title-blue); font-size: 42px; letter-spacing: 2px; text-anchor: middle; }
</style>
</head>
<body>
<svg width="0" height="0" style="position:absolute">
  <defs>
    <symbol id="label-base" viewBox="0 0 450 540">
      <polygon class="house-shape" points="0,207 237,2 437,222 400,255 263,115 30,318 30,377 430,377 430,527 0,527"/>
      <rect class="brand-mark" x="2" y="64" width="24" height="24"/>
      <text class="brand-name" x="36" y="88">LindenHaus</text>
      <polygon fill="var(--class-a)" points="135,215 280,215 292,228 280,241 135,241"/>
      <text class="bar-letter" x="257" y="235">A</text>
      <polygon fill="var(--class-b)" points="135,246 289,246 301,259 289,272 135,272"/>
      <text class="bar-letter" x="256" y="266">B</text>
      <polygon fill="var(--class-c)" points="135,277 298,277 310,290 298,303 135,303"/>
      <text class="bar-letter" x="255" y="297">C</text>
      <polygon fill="var(--class-d)" points="135,308 307,308 319,321 307,334 135,334"/>
      <text class="bar-letter" x="256" y="328">D</text>
      <polygon fill="var(--class-e)" points="135,339 316,339 328,352 316,365 135,365"/>
      <text class="bar-letter" x="255" y="359">E</text>
      <polygon fill="var(--class-f)" points="135,370 325,370 337,383 325,396 135,396"/>
      <text class="bar-letter" x="255" y="390">F</text>
      <polygon fill="var(--class-g)" points="135,401 334,401 346,414 334,427 135,427"/>
      <text class="bar-letter" x="256" y="421">G</text>
      <text class="caption" x="414" y="456">Berechneter Energiebedarf</text>
      <text class="title" x="216" y="507">ENERGIEAUSWEIS</text>
    </symbol>
  </defs>
</svg>

<main class="canvas">
  <svg class="label-card" style="left:46px;top:32px" viewBox="0 0 450 540">
    <use href="#label-base"/>
    <rect class="figure-area" role="img" aria-label="Blaues Männchen trägt die Energieskala mit rotem Haus" x="12" y="212" width="150" height="200" rx="30"/>
    <polygon class="marker-shape" points="340,228 352,217 410,217 410,239 352,239"/>
    <text class="marker-letter" x="394" y="235">A</text>
  </svg>

  <svg class="label-card" style="left:622px;top:30px" viewBox="0 0 450 540">
    <use href="#label-base"/>
    <rect class="figure-area" role="img" aria-label="Blaues Männchen trägt die Energieskala mit rotem Haus" x="12" y="212" width="150" height="200" rx="30"/>
    <polygon class="marker-shape" points="340,259 352,248 410,248 410,270 352,270"/>
    <text class="marker-letter" x="394" y="266">B</text>
  </svg>

  <svg class="label-card" style="left:49px;top:733px" viewBox="0 0 450 540">
    <use href="#label-base"/>
    <rect class="figure-area" role="img" aria-label="Blaues Männchen trägt die Energieskala mit rotem Haus" x="12" y="212" width="150" height="200" rx="30"/>
    <polygon class="marker-shape" points="340,290 352,279 410,279 410,301 352,301"/>
    <text class="marker-letter" x="394" y="297">C</text>
  </svg>

  <svg class="label-card" style="left:639px;top:730px" viewBox="0 0 450 540">
    <use href="#label-base"/>
    <rect class="figure-area" role="img" aria-label="Blaues Männchen trägt die Energieskala mit rotem Haus" x="12" y="212" width="150" height="200" rx="30"/>
    <polygon class="marker-shape" points="340,321 352,310 410,310 410,332 352,332"/>
    <text class="marker-letter" x="394" y="328">D</text>
  </svg>

  <svg class="label-card" style="left:52px;top:1434px" viewBox="0 0 450 540">
    <use href="#label-base"/>
    <rect class="figure-area" role="img" aria-label="Blaues Männchen trägt die Energieskala mit rotem Haus" x="12" y="212" width="150" height="200" rx="30"/>
    <polygon class="marker-shape" points="340,352 352,341 410,341 410,363 352,363"/>
    <text class="marker-letter" x="394" y="359">E</text>
  </svg>

  <svg class="label-card" style="left:651px;top:1435px" viewBox="0 0 450 540">
    <use href="#label-base"/>
    <rect class="figure-area" role="img" aria-label="Blaues Männchen trägt die Energieskala mit rotem Haus" x="12" y="212" width="150" height="200" rx="30"/>
    <polygon class="marker-shape" points="340,383 352,372 410,372 410,394 352,394"/>
    <text class="marker-letter" x="394" y="390">F</text>
  </svg>

  <svg class="label-card" style="left:58px;top:2138px" viewBox="0 0 450 540">
    <use href="#label-base"/>
    <rect class="figure-area" role="img" aria-label="Blaues Männchen trägt die Energieskala mit rotem Haus" x="12" y="212" width="150" height="200" rx="30"/>
    <polygon class="marker-shape" points="350,414 362,403 420,403 420,425 362,425"/>
    <text class="marker-letter" x="404" y="421">G</text>
  </svg>
</main>
</body>
</html>
```